nutrition ebook cover

i need a cover for a ebook designed, the book is called Amber Lattice so i would like that somewhere on the cover. i would also like the word nutrition followed by my company logo that i have attached below somewhere on the cover( i have attached two logos and would like to see with both separatley), i would like this to be faded into the background if possible, perhaps in a upper or lower corner. i would also like to see options with and without the picture i have attached below. the look I'm going for is professional and clean. this is a fat loss, healthy eating booklet. the winning designer i would like to design the following pages within the book aswell no more than 10 pages, that i will provide all content for, i just need help with putting what i have on pdf in a way that looks professional and cool. this would ideally covered in the rate that is paid for the cover. i also have other booklets i need made so the winning designer will most likely get that work too at a later date for an additional fee of course.

Industry/Entity Type

Nutrition

Requirements
Nice to have
• Outside images are welcomed, happy to purchase any stock images used from a outside source

```html
<!DOCTYPE html>
<html lang="en">
<head>
<meta charset="utf-8">
<title>Amber Lattice – Ebook Cover</title>
<link rel="stylesheet" href="https://fonts.googleapis.com/css2?family=Cinzel:wght@700;900&family=Oswald:wght@600&display=swap">
<style>
  :root {
    --slate: #252a33;
    --wood-light: #c0773f;
    --wood-mid: #9a5428;
    --wood-dark: #5a3018;
    --table: #33464a;
    --table-dark: #223033;
    --leaf: #3f6a2c;
    --tomato: #8a3a26;
    --title: #ffffff;
    --rule: #f2c511;
    --badge-bg: #23402a;
    --badge-text: #0f150f;
  }
  * { margin: 0; padding: 0; box-sizing: border-box; }
  html, body { width: 800px; height: 1200px; overflow: hidden; background: var(--slate); }
  .cover { position: relative; width: 800px; height: 1200px; background: var(--slate); overflow: hidden; }
  .cover-photo {
    position: absolute; left: 0; top: 168px; width: 800px; height: 870px;
    background:
      radial-gradient(ellipse 58% 50% at 53% 60%, var(--wood-light) 0%, var(--wood-mid) 45%, var(--wood-dark) 72%, rgba(90,48,24,0) 86%),
      radial-gradient(ellipse 30% 22% at 10% 92%, rgba(63,106,44,0.85) 0%, rgba(63,106,44,0) 100%),
      radial-gradient(ellipse 14% 22% at 97% 65%, rgba(63,106,44,0.8) 0%, rgba(63,106,44,0) 100%),
      radial-gradient(ellipse 30% 18% at 35% 12%, rgba(214,206,186,0.45) 0%, rgba(214,206,186,0) 100%),
      radial-gradient(ellipse 25% 15% at 80% 14%, rgba(160,120,80,0.45) 0%, rgba(160,120,80,0) 100%),
      radial-gradient(ellipse 10% 10% at 92% 97%, rgba(138,58,38,0.7) 0%, rgba(138,58,38,0) 100%),
      linear-gradient(160deg, var(--table) 0%, var(--table-dark) 100%);
  }
  .title-main, .title-sub {
    position: absolute; left: 0; width: 800px; text-align: center;
    font-family: "Cinzel", serif; font-weight: 900; color: var(--title);
    text-shadow: 3px 3px 4px rgba(0,0,0,0.6); line-height: 1;
  }
  .title-main { top: 532px; font-size: 124px; padding-left: 44px; }
  .title-sub { top: 676px; font-size: 80px; letter-spacing: 3px; padding-left: 44px; }
  .title-rule {
    position: absolute; left: 168px; top: 766px; width: 500px; height: 3px; background: var(--rule);
  }
  .brand-badge {
    position: absolute; left: 0; top: 1076px; width: 270px; height: 70px;
    background: var(--badge-bg); display: flex; align-items: center; padding-left: 10px;
  }
  .brand-name {
    font-family: "Oswald", sans-serif; font-weight: 600; font-size: 36px;
    color: var(--badge-text); letter-spacing: 0.5px; line-height: 1;
  }
</style>
</head>
<body>
  <main class="cover">
    <div class="cover-photo" role="img" aria-label="Old wooden cutting board on a dark table surrounded by fresh vegetables, mushrooms, tomatoes, lemon, herbs and spices"></div>
    <h1 class="title-main">AMBER</h1>
    <p class="title-sub">LATTICE</p>
    <div class="title-rule"></div>
    <div class="brand-badge">
      <span class="brand-name">VERDANT MARK</span>
    </div>
  </main>
</body>
</html>
```